Cruise Booking Website

Cruise search and booking website

This project is a redesign of a cruise booking website we did a few years ago.

The current website is located here: http://voyage.pixelmarsh.com/en/

It's not fully functional but gives you ad idea how miserable the old design was.

All the information about cruises, cruise lines, destinations, ports and shore excursions will be similar to http://www.sailorbay.com/
Actual search pages (form, results, single result, sailing and cabin selection, ship info, booking) will have EXACTLY the same info as sailorbay.com

We like the style of http://harborvoyagehub.com, it's quite modern, good spacing, not overloaded with information. So you can use it as an example of what we like, not what we want as a final result for us. Please, don't copy it. The result should not be possible to resemble the harborvoyagehub.com, because our site has to be unique. This is important!
If you submit a design that clearly reminds another cruise site it will be rejected!

Also the mockup provided is just to give you the basic structure and show what information has to be present on the page. It doesn't mean the layout has to be the same as a mockup. The layout is up to the designer.

I've updated the mockup to be more generic so it doesn't confuse you:
https://www.filecrate.net/s/k7q2mz9pw4tnb3x/Home%20page.png

When you're adding social sharing icons like chatterbox/peeplet you have to use chinese ones instead:
https://www.filecrate.net/s/h3rt8wyd6jcl0fe/chinese-social-icons.png
Originals: http://shrtlk.example/qRmT

We'll start with home page first and after it's approved inner pages can be designed.

I know the cost of the project doesn't look high, but the task is straight forward and doesn't require to be very original, it's better to follow existing design and layout patterns that proved to work well.
That's why I encourage you to choose a template to build the design on top of one of https://themequarry.net/ themes if it will save the design work, will be easier and faster for you. So it will be more like a customization than a new design from scratch.

Mockups, site map and logo files:
- https://www.filecrate.net/sh/50xb7vq1ndtpkez/RmwuHp8Zq3

Website tree:
- https://papers.quillnet.example/document/d/8vTrXk2MqLpZ4wNsB7yHcE1oUjFgD9aR_QbVtnWm/edit?usp=sharing
Updates

So far a lot of designs are just copying http://www.harborvoyagehub.com/ - we don't like it!

We like the style of harborvoyagehub.com, it's quite modern, good spacing, not overloaded with information. So you can use it as an example of what we like, not what we want as a final result for us. Please, don't copy it. The result should not be possible to resemble the harborvoyagehub.com, because our site has to be unique. This is important!

Target Market(s)

Chinese travellers

Industry/Entity Type

Build

Requirements
Must have
• * White, blue and red
* Large spacing, not too much information cramped into a small space like sailorbay.com or the current website
* More "hidden" info in popups, tabs and so on, so not to many things are visible at the same time
* Compatible with lumen framekit styling (for easier coding):
- http://lumenkit.example.io/framework/index.html
- http://skinvault.net/
* Feel free to propose to build the design on top of one of https://themequarry.net/ themes if it will save the design work, will be easier and faster for you

```html
<!DOCTYPE html>
<html lang="en">
<head>
<meta charset="utf-8">
<title>Tidewell Cruises – Home</title>
<link href="https://fonts.googleapis.com/css2?family=Open+Sans:wght@400;600;700&family=Ubuntu:wght@400;500&display=swap" rel="stylesheet">
<style>
:root{
  --topbar:#2e3033;
  --nav-orange:#f6a700;
  --nav-orange-light:#ffd23a;
  --nav-text:#5a3a00;
  --red:#c8202f;
  --blue:#1f7fbf;
  --blue-dark:#1b4a75;
  --search-band:#2a97d1;
  --strip:#3a3c3f;
  --content-bg:#e9e9e9;
  --text:#3d3d3d;
  --muted:#6c6c6c;
  --footer:#a4cbea;
  --footer-strip:#aed2ee;
  --white:#ffffff;
}
*{box-sizing:border-box;margin:0;padding:0}
html,body{width:1200px;height:960px;overflow:hidden;background:var(--white)}
body{font-family:"Open Sans",Arial,sans-serif;color:var(--text);position:relative}
.page{position:relative;width:1200px;height:960px;overflow:hidden}
.abs{position:absolute}

/* top utility bar */
.utility-bar{left:0;top:0;width:1200px;height:17px;background:var(--topbar)}
.utility-links{left:666px;top:3px;font-size:8px;color:#cfd3d8;display:flex;gap:46px}
.utility-social{left:933px;top:4px;display:flex;gap:5px}
.utility-social span{width:8px;height:8px;background:#9ec6e6;border-radius:2px}

/* main nav */
.main-nav{left:0;top:17px;width:1200px;height:22px;background:linear-gradient(var(--nav-orange-light),var(--nav-orange));border-bottom:1px solid #d98c00}
.main-nav ul{list-style:none;position:absolute;left:0;top:0;height:22px}
.main-nav li{position:absolute;top:0;height:22px;line-height:22px;font-size:12px;color:var(--nav-text);font-family:"Ubuntu",sans-serif}
.main-nav li.active{background:var(--red);color:var(--white);padding:0 7px}
.main-nav .sep{position:absolute;top:3px;width:1px;height:16px;background:#d28a00}

/* hero */
.hero{left:0;top:39px;width:1200px;height:280px;background:linear-gradient(180deg,#0d5ea5 0%,#3a8fd0 38%,#a9d3ef 62%,#4f93c6 74%,#0f5a8e 100%)}
.hero-ship{left:485px;top:150px;width:640px;height:130px;background:linear-gradient(180deg,#e8eef3,#b8c7d4);border-radius:60px 8px 4px 30px;opacity:.85}
.slider-dots{left:925px;top:46px;display:flex;gap:4px}
.slider-dots span{width:4px;height:4px;border-radius:50%;background:#7fb2d8}
.slider-dots span:first-child{background:#fff}
.promo-line{left:591px;top:39px;width:1px;height:43px;background:var(--red)}
.promo-badge{left:559px;top:82px;width:66px;height:54px;border-radius:50%;background:var(--red);color:#fff;text-align:center;box-shadow:0 2px 4px rgba(0,0,0,.3)}
.promo-badge small{display:block;font-size:8px;margin-top:11px;letter-spacing:.5px}
.promo-badge strong{font-size:15px;font-weight:700}
.promo-badge em{font-style:normal;font-size:8px}
.promo-caption{left:534px;top:141px;font-size:9px;color:#fff}

/* brand */
.brand{left:244px;top:202px;width:119px;height:117px;background:linear-gradient(#fff,#e9eef2);border:1px solid #d0d6db;display:flex;flex-direction:column;align-items:center;justify-content:center;gap:8px}
.brand-mark{width:26px;height:26px;border-radius:50%;background:var(--blue)}
.brand-name{font-family:"Ubuntu",sans-serif;font-weight:500;font-size:20px;color:var(--blue-dark)}

/* search */
.search-tabs{left:0;top:319px;width:1200px;height:20px;background:var(--strip)}
.search-tabs ul{list-style:none}
.search-tabs li{position:absolute;top:3px;font-size:9px;color:#d9dcdf}
.search-tabs li.active{color:#fff}
.search-tabs li.active::after{content:"";position:absolute;left:50%;margin-left:-5px;top:14px;border:5px solid transparent;border-top-color:var(--strip)}
.phone{left:775px;top:1px;font-size:15px;color:#fff;font-family:"Ubuntu",sans-serif;display:flex;align-items:center;gap:5px}
.search-band{left:0;top:339px;width:1200px;height:40px;background:linear-gradient(#3aa5dc,#1f86c2)}
.select{position:absolute;top:9px;height:16px;border:1px solid #0e5c8f;background:#1a76b0;color:#fff;font-size:8px;line-height:14px;padding-left:5px}
.select::after{content:"";position:absolute;right:0;top:0;width:14px;height:14px;border-left:1px solid #0e5c8f;background:linear-gradient(135deg,transparent 45%,#fff 45%,#fff 55%,transparent 55%) no-repeat 3px 4px/4px 4px,linear-gradient(45deg,transparent 45%,#fff 45%,#fff 55%,transparent 55%) no-repeat 7px 4px/4px 4px}
.wheel{left:894px;top:325px;width:50px;height:50px;border-radius:50%;background:radial-gradient(circle,#fff 30%,#d9ecf8 31%,#fff 60%)}

/* content */
.content{left:0;top:379px;width:1200px;height:331px;background:var(--content-bg)}
.tab{position:absolute;top:392px;height:22px;font-size:9px;line-height:22px;text-align:center;border:1px solid #c9c9c9;border-bottom:none}
.tab-featured{left:244px;width:110px;background:#f3f3f3;color:var(--blue-dark);font-weight:600}
.tab-offers{left:356px;width:110px;background:#e0e0e0;color:var(--muted)}
.tab-rule{left:244px;top:414px;width:463px;height:1px;background:#c9c9c9}
.feature-photo{left:244px;top:434px;width:234px;height:121px;border:3px solid #fff;background:linear-gradient(160deg,#3b86b8 0%,#76b8d5 35%,#e7dcb5 55%,#4f8a4d 75%,#2f6c44 100%);box-shadow:0 1px 2px rgba(0,0,0,.2)}
.feature-title{left:506px;top:428px;font-family:"Ubuntu",sans-serif;font-size:17px;color:var(--red)}
.feature-points{left:506px;top:449px;font-size:8px;color:var(--blue);display:flex;align-items:center;gap:6px}
.feature-list{left:506px;top:477px;list-style:none;font-size:8.5px;color:var(--red)}
.feature-list li{height:18px;display:flex;align-items:center;gap:6px}
.feature-list li b{font-size:13px;font-weight:400}
.share{left:601px;top:544px;display:flex;align-items:center;gap:3px;font-size:8px;color:var(--text)}
.share span{width:10px;height:10px;background:#d64a3a;border-radius:2px}
.share span.alt{background:#2f7fc0}
.feature-text{left:244px;top:568px;width:440px;font-size:9px;line-height:18px;color:var(--text)}
.feature-text a{color:var(--blue);font-weight:700;text-decoration:none;margin-left:12px}
.pager{left:439px;top:655px;display:flex;gap:3px}
.pager span{width:5px;height:5px;border-radius:50%;background:#cfcfcf}
.pager span:first-child{background:var(--blue)}
.divider{left:720px;top:395px;width:1px;height:300px;background:#cfcfcf}

.offer-card{left:756px;top:396px;width:200px;height:97px;border:3px solid #fff;background:linear-gradient(90deg,#d6a888 0%,#e07a5e 30%,#b7c9d8 55%,#2b4662 60%,#1e3a58 100%);box-shadow:0 1px 3px rgba(0,0,0,.25)}
.offer-copy{left:875px;top:418px;color:#fff;text-align:right;width:70px}
.offer-copy small{display:block;font-size:8px}
.offer-copy strong{display:block;font-size:18px;font-weight:400;line-height:18px}
.offer-copy em{display:block;font-style:normal;font-size:7px}
.offer-flag{left:734px;top:466px;width:78px;height:26px;background:var(--red);color:#fff;font-size:10px;font-weight:700;text-align:center;line-height:26px;border-radius:4px 14px 14px 4px}
.newsletter-title{left:733px;top:520px;width:226px;text-align:center;font-family:"Ubuntu",sans-serif;font-size:16px;color:var(--blue-dark)}
.newsletter-rule{left:733px;top:541px;width:226px;height:1px;background:#9db9cf}
.newsletter-text{left:733px;top:549px;width:226px;font-size:8px;line-height:12px;color:var(--blue)}
.field{position:absolute;left:733px;width:224px;height:18px;border-bottom:1px solid #b7c7d4;font-size:8px;color:var(--blue-dark);line-height:16px}
.subscribe{left:864px;top:667px;width:92px;height:15px;border-top:2px solid var(--blue);font-size:8px;text-align:center;line-height:13px;color:var(--blue-dark);font-weight:600}
.privacy{left:885px;top:686px;font-size:6px;color:var(--muted)}

/* partner lines */
.lines-strip{left:0;top:710px;width:1200px;height:55px;background:var(--footer-strip);border-bottom:1px solid #96bddc}
.strip-arrow{position:absolute;top:731px;width:13px;height:13px;border-radius:50%;background:#d3e4f2;border:1px solid #8fb2cd;font-size:8px;text-align:center;line-height:11px;color:#4b6a85}
.line-names{left:262px;top:729px;width:680px;display:flex;justify-content:space-between;font-family:"Ubuntu",sans-serif;font-size:13px;color:var(--blue-dark)}

/* footer */
.footer{left:0;top:765px;width:1200px;height:195px;background:var(--footer)}
.footer-col{position:absolute;top:774px}
.footer-col h3{font-family:"Ubuntu",sans-serif;font-weight:400;font-size:11px;color:var(--blue-dark);border-bottom:1px solid var(--blue-dark);padding-bottom:2px;margin-bottom:8px;display:inline-block;padding-right:8px}
.footer-col ul{list-style:none;font-size:8.5px;color:#1f2e3b}
.footer-col li{height:14.4px}
.see-all{display:flex;align-items:center;gap:5px;font-size:10px;color:var(--blue-dark);margin-top:1px}
.see-all i{width:9px;height:9px;border-radius:50%;background:var(--blue-dark);display:inline-block}
.contact-box{left:754px;top:778px;width:202px;height:106px;background:var(--blue-dark);color:#fff;font-size:8px}
.contact-row{position:absolute;left:12px;top:18px;display:flex;gap:26px}
.follow{position:absolute;left:12px;top:38px;display:flex;align-items:center;gap:8px}
.follow span{font-size:7px;background:#fff;color:var(--blue-dark);padding:1px 3px}
.contact-brand{position:absolute;left:0;top:66px;width:202px;text-align:center;font-family:"Ubuntu",sans-serif;font-size:13px;color:#cfd8e0}
.copyright{left:0;top:940px;width:1200px;text-align:center;font-size:7px;letter-spacing:1.5px;color:var(--blue-dark)}
</style>
</head>
<body>
<div class="page">

  <div class="abs utility-bar"></div>
  <div class="abs utility-links"><span>Location Finder</span><span>My Account</span></div>
  <div class="abs utility-social"><span></span><span></span></div>

  <nav class="abs main-nav">
    <ul>
      <li class="active" style="left:244px">Blog</li>
      <li style="left:311px">Cruise Info</li>
      <li style="left:408px">Specialty Cruises</li>
      <li style="left:540px">Destinations</li>
      <li style="left:652px">Lines</li>
      <li style="left:719px">Deals</li>
      <li style="left:789px">Ports</li>
      <li style="left:855px">Quote Request</li>
    </ul>
    <span class="sep" style="left:388px"></span>
    <span class="sep" style="left:523px"></span>
    <span class="sep" style="left:633px"></span>
    <span class="sep" style="left:700px"></span>
    <span class="sep" style="left:767px"></span>
    <span class="sep" style="left:835px"></span>
    <span class="sep" style="left:950px"></span>
  </nav>

  <section class="abs hero" role="img" aria-label="Large cruise ship sailing on a bright blue sea under a clear sky with white clouds"></section>
  <div class="abs hero-ship" role="img" aria-label="White cruise liner"></div>
  <div class="abs slider-dots"><span></span><span></span><span></span><span></span></div>
  <div class="abs promo-line"></div>
  <div class="abs promo-badge"><small>SAVE</small><strong>40%</strong> <em>off</em></div>
  <div class="abs promo-caption">Lorem ipsum dolor sit amet &nbsp;›</div>

  <div class="abs brand">
    <span class="brand-mark"></span>
    <span class="brand-name">Tidewell</span>
  </div>

  <div class="abs search-tabs">
    <ul>
      <li class="active" style="left:251px">Cruises</li>
      <li style="left:300px">Air</li>
      <li style="left:332px">Hotel</li>
      <li style="left:374px">Car</li>
    </ul>
    <div class="abs phone">
      <svg width="10" height="10" viewBox="0 0 10 10"><path d="M2 1h2l1 2-1.2 1a5 5 0 0 0 2.2 2.2L7 5l2 1v2c0 .6-.4 1-1 1A8 8 0 0 1 1 2c0-.6.4-1 1-1z" fill="#fff"/></svg>
      4008 512 930
    </div>
  </div>
  <form class="abs search-band">
    <div class="select" style="left:242px;width:120px">Caribbean/Bahamas</div>
    <div class="select" style="left:375px;width:88px">All Ports</div>
    <div class="select" style="left:476px;width:101px">All Cruise Lines</div>
    <div class="select" style="left:589px;width:119px">All Ships</div>
    <div class="select" style="left:721px;width:74px">August 2013</div>
    <div class="select" style="left:801px;width:69px">All Length</div>
  </form>
  <div class="abs wheel" role="img" aria-label="Ship steering wheel emblem"></div>

  <main class="abs content"></main>
  <div class="tab tab-featured">FEATURED</div>
  <div class="tab tab-offers">Exceptional Offers</div>
  <div class="abs tab-rule"></div>

  <div class="abs feature-photo" role="img" aria-label="Tropical beach resort with palm trees, pools and turquoise sea"></div>
  <h2 class="abs feature-title">Japan 8 days</h2>
  <div class="abs feature-points">
    <svg width="8" height="8" viewBox="0 0 8 8"><rect x="0" y="3" width="8" height="5" fill="#c8202f"/><rect x="3.3" y="0" width="1.4" height="8" fill="#f6a700"/></svg>
    This trip can earn you: 3000 points
  </div>
  <ul class="abs feature-list">
    <li>›&nbsp; Special rates for guests 55 years and older</li>
    <li>›&nbsp; Rates from <b>$209</b></li>
    <li>›&nbsp; Kids 11 and Under Sail Free</li>
  </ul>
  <div class="abs share"><span></span>Share <span></span><span class="alt"></span></div>
  <p class="abs feature-text">Lorem ipsum dolor sit amet, consectetur adipiscing elit. Ut lobortis leo et sem mattis vel tempus nibh egestas. Suspendisse fermentum pharetra nisi, eget bibendum elit ultricies ut. Nullam congue venenatis imperdiet. Proin enim purus, malesuada vitae congue eu, fermentum vel metus. Mauris scelerisque sodales viverra. Proin hendrerit scelerisque orci<a href="#">READ DETAILS</a></p>
  <div class="abs pager"><span></span><span></span><span></span><span></span><span></span><span></span></div>
  <div class="abs divider"></div>

  <div class="abs offer-card" role="img" aria-label="Couple relaxing on a cruise deck"></div>
  <div class="abs offer-copy"><small>Enter &amp; Win</small><strong>$ 6000</strong><strong>CRUISE</strong><em>Vacation For 2</em></div>
  <div class="abs offer-flag">Best Offer</div>

  <h2 class="abs newsletter-title">Tidewell Deals Newsletter</h2>
  <div class="abs newsletter-rule"></div>
  <p class="abs newsletter-text">Sign up for our newsletter and receive our best deals in your inbox.</p>
  <div class="field" style="top:580px">YOUR NAME</div>
  <div class="field" style="top:598px">YOUR E-MAIL</div>
  <div class="field" style="top:616px">YOUR PHONE NUMBER</div>
  <div class="field" style="top:634px">YOUR POSTAL &nbsp;/ ZIP CODE</div>
  <div class="abs subscribe">SUBCRIBE</div>
  <div class="abs privacy">Privacy Policy / Rules</div>

  <div class="abs lines-strip"></div>
  <div class="strip-arrow" style="left:243px">‹</div>
  <div class="strip-arrow" style="left:943px">›</div>
  <div class="abs line-names">
    <span>Amberly</span><span>Corvina</span><span>Stellaris</span><span>Cortella</span><span>Meridane</span><span>Fablesea</span><span>Lowland Line</span><span>Marevia</span>
  </div>

  <footer class="abs footer"></footer>
  <div class="footer-col" style="left:242px">
    <h3>FAMOUS CRUISE LINES</h3>
    <ul><li>World Cruise Lines</li><li>World Cruise Lines</li><li>World Cruise Lines</li><li>World Cruise Lines</li><li>World Cruise Lines</li></ul>
    <div class="see-all"><i></i>SEE ALL</div>
  </div>
  <div class="footer-col" style="left:425px">
    <h3>FAMOUS DESTINATIONS</h3>
    <ul><li>Middle East</li><li>South America</li><li>Bermuda</li><li>Australia &amp; New Zealand</li><li>North America</li></ul>
    <div class="see-all"><i></i>SEE ALL</div>
  </div>
  <div class="footer-col" style="left:614px">
    <h3>SHORES Activities</h3>
    <ul><li>Europe</li><li>Panama Canal</li><li>Mexico</li><li>South America</li><li>Bermuda</li></ul>
    <div class="see-all"><i></i>SEE ALL</div>
  </div>

  <div class="abs contact-box">
    <div class="contact-row"><span>☏ 4008 512 930</span><span>✉ &nbsp;info@tidewell.com</span></div>
    <div class="follow">Follow Us On: <span>chatterbox</span><span>peeplet</span></div>
    <div class="contact-brand">Tidewell</div>
  </div>

  <div class="abs copyright">Copyright © 2011 tidewell.com All Rights Reserved</div>
</div>
</body>
</html>
```